Revamp Landing Page

Our current landing page is http://lanternpubkq.com/ and we're looking for our site to look like this http://www.amberroomvk.com/. Classy, Sleek, Simple elegant.

The site should be desktop and mobile optimized.
Pages should be built out and the same structure. Drink Menu, Gallery, Events, Table Reservations, Membership, Press, Contact Us.

Feel free to use the images on our website.

```html
<!DOCTYPE html>
<html lang="en">
<head>
<meta charset="utf-8">
<title>Lantern Pub</title>
<link rel="stylesheet" href="https://fonts.googleapis.com/css2?family=Open+Sans:wght@400;600;700&display=swap">
<style>
:root{
  --page:#f9efeb;
  --band:#f3e4df;
  --white:#ffffff;
  --gold:#a08659;
  --gold-text:#9a8058;
  --ink:#2a2522;
  --line:#cdbfb7;
}
*{margin:0;padding:0;box-sizing:border-box}
html,body{width:1200px;height:780px;overflow:hidden}
body{background:var(--page);font-family:"Open Sans",sans-serif;color:var(--ink);position:relative}
.pattern{position:absolute;left:0;top:0;width:1200px;height:667px;background:radial-gradient(ellipse at 50% 40%,#fbf4f1 0%,var(--page) 70%)}
.brand{position:absolute;left:0;top:38px;width:1200px;text-align:center;font-size:38px;font-weight:400;letter-spacing:4px;color:var(--ink)}
.frame{position:absolute;left:186px;top:115px;width:826px;height:504px;border:1px solid var(--line)}
.nav{position:absolute;left:278px;top:105px;width:644px;height:22px;background:var(--page);display:flex;justify-content:center;gap:19px;align-items:center}
.nav a{font-size:10.5px;letter-spacing:1.3px;color:var(--ink);text-decoration:none}
.photo{position:absolute}
.p-lounge-lamp{left:222px;top:145px;width:183px;height:172px;background:linear-gradient(160deg,#5a3a1c,#c48a45 55%,#7a4a22)}
.p-dj{left:222px;top:326px;width:183px;height:218px;background:linear-gradient(170deg,#1c2448,#2a3f7a 55%,#0f1430)}
.p-boat{left:414px;top:145px;width:320px;height:205px;background:linear-gradient(120deg,#4d3a2c,#b5a79a 50%,#7a6d66)}
.p-booth{left:414px;top:361px;width:451px;height:225px;background:linear-gradient(165deg,#6a4122,#c98a49 50%,#5a2f17)}
.p-bar{left:872px;top:361px;width:105px;height:225px;background:linear-gradient(180deg,#e8dcc0,#7a4a2c 45%,#2a1a14)}
.intro{position:absolute;left:743px;top:145px;width:234px;height:204px;background:var(--gold);color:var(--white);padding:48px 30px 0 32px}
.intro h1{font-size:12.4px;font-weight:700;line-height:14.5px;text-transform:uppercase;margin-bottom:8px}
.intro p{font-size:10.2px;line-height:12.6px}
.reserve{position:absolute;left:222px;top:552px;width:182px;height:34px;background:var(--gold);color:var(--white);font-size:9.6px;font-weight:700;letter-spacing:1.6px;display:flex;align-items:center;justify-content:center}
.social{position:absolute;left:346px;top:609px;width:510px;height:20px;background:var(--page);display:flex;justify-content:center;align-items:center;gap:14px}
.social span{display:flex;align-items:center;gap:8px;font-size:10px;letter-spacing:1.2px;color:var(--gold-text)}
.social i{display:block;width:10px;height:10px;border-radius:50%;background:var(--gold-text)}
.promo{position:absolute;left:0;top:667px;width:1200px;height:42px;background:var(--band);display:flex;justify-content:center;align-items:center;font-size:12.4px;gap:6px}
.promo a{color:var(--ink);font-weight:700;text-decoration:underline}
.footer{position:absolute;left:0;top:709px;width:1200px;height:71px;background:var(--white);text-align:center;padding-top:28px;font-size:10.4px;letter-spacing:1.2px}
</style>
</head>
<body>
<div class="pattern" role="img" aria-label="Faint swirling paisley background pattern"></div>
<div class="brand">LANTERN PUB</div>
<div class="frame"></div>
<nav class="nav">
  <a href="#">DRINK MENU</a><a href="#">GALLERY</a><a href="#">EVENTS</a><a href="#">TABLE RESERVATIONS</a><a href="#">MEMBERSHIP</a><a href="#">PRESS</a><a href="#">CONTACT US</a>
</nav>
<div class="photo p-lounge-lamp" role="img" aria-label="Warm lounge booth with table lamp and board game"></div>
<div class="photo p-dj" role="img" aria-label="DJ booth with glowing blue decks"></div>
<div class="photo p-boat" role="img" aria-label="Boat-hull styled entrance wall under red light"></div>
<section class="intro">
  <h1>Lantern Pub: a home away from home for the local community.</h1>
  <p>At Lantern Pub, it is our goal to make sure that you enjoy every moment in your experience. Consider us your liaisons to happiness...</p>
</section>
<div class="photo p-booth" role="img" aria-label="Large lounge seating area with lamps and beach mural"></div>
<div class="photo p-bar" role="img" aria-label="Back bar shelves lined with bottles"></div>
<div class="reserve">TABLE RESERVATIONS</div>
<div class="social">
  <span><i></i>FOLLOW ON FRIENDBOOK</span>
  <span><i></i>FOLLOW ON CHIRPER</span>
  <span><i></i>FOLLOW ON SNAPGRAM</span>
</div>
<div class="promo">Want to Book a Private Party? <a href="#">Check Out Our Events Deck</a></div>
<footer class="footer">48 Harbor Ln Westport, California 90811 info@lanternpubkq.com</footer>
</body>
</html>
```